Healthcare Comms Consultant Needs Scroll Down Website

Would like a modern scroll down website/ site on one page. Would like a gallery at the top. Followed by my bio and capabilities section. Pretty simple. Just want it look pretty/ clean. Example of similar site - https://7qrstudio.com. I live in San Diego so would be neat to bring in some water elements. And I surf.

Target Market(s)

US biotech, Medtech companies

Industry/Entity Type

Healthcare

Coding

Coded - Design and coding required

Number of Pages Required

1 page

Font styles to use
Sans Serif

Requirements
Must have
• A logo, gallery section (I have the photos) with one large pic of me in the center (Brintex), short list of capabilities (I have text), my bio (I have this text). How to contact me at the bottom and a link to my Proflume profile.

```html
<!DOCTYPE html>
<html lang="en">
<head>
<meta charset="utf-8">
<title>Harbor Lane Media – Website Layouts</title>
<link rel="stylesheet" href="https://fonts.googleapis.com/css2?family=Varela+Round&family=Montserrat:wght@400;500;600&family=Great+Vibes&family=Roboto:wght@900&display=swap">
<style>
:root{
  --stage:#6e6e6e;
  --white:#ffffff;
  --navy:#2b3590;
  --ink:#2d3a8c;
  --blue:#0fa0e6;
  --blue-deep:#2350a8;
  --text:#6a6a6a;
  --ghost:#f3f3f6;
  --field:#ececec;
  --photo-a:#5a6fc4;
  --photo-b:#c9a27c;
}
*{box-sizing:border-box;margin:0;padding:0}
html,body{width:1073px;height:1200px;overflow:hidden;background:var(--stage)}
.stage{position:absolute;left:0;top:0;width:1820px;height:2036px;transform:scale(.58956);transform-origin:0 0;background:var(--stage);font-family:"Montserrat",sans-serif}
.page{position:absolute;top:93px;width:804px;background:var(--white);overflow:hidden}
.page--hex{left:84px;height:1850px}
.page--grid{left:932px;height:1670px}
.content{position:absolute;left:0;width:804px;height:1850px}
.page--grid .content{top:-180px}

/* header (hex layout) */
.brand{position:absolute;display:flex;align-items:center;gap:8px;font-family:"Varela Round",sans-serif;color:var(--blue)}
.brand__mark{width:46px;height:46px;background:var(--blue)}
.brand__name{font-size:17px;line-height:16px}
.page--hex .brand{left:161px;top:15px}
.social{position:absolute;display:flex;gap:5px}
.social__dot{width:22px;height:22px;border-radius:50%;background:var(--ink)}
.social__dot--b{background:var(--blue)}
.social__dot--c{background:#e3263a}
.page--hex .social{left:536px;top:15px}
.burger{position:absolute;left:637px;top:18px;width:20px;height:16px;border-top:3px solid #222;border-bottom:3px solid #222}
.burger::after{content:"";position:absolute;left:0;right:0;top:3.5px;border-top:3px solid #222}
.hexes{position:absolute;left:0;top:0}
.arrow{position:absolute;font-size:14px;color:#222;font-family:"Montserrat",sans-serif}

/* sidebar (grid layout) */
.sidebar{position:absolute;left:0;top:0;width:95px;height:318px;background:var(--navy)}
.sidebar__brand{height:60px;background:var(--blue);display:flex;align-items:center;padding-left:6px;gap:4px;font-family:"Varela Round",sans-serif;color:var(--white);font-size:10px;line-height:10px}
.sidebar__mark{width:14px;height:14px;background:var(--white)}
.menu{list-style:none;margin-top:17px}
.menu li{height:34px;padding-left:20px;font-size:10px;color:var(--white);border-bottom:1px solid rgba(255,255,255,.08);line-height:26px}
.search{position:absolute;left:22px;top:232px;width:20px;height:20px;border-radius:50%;background:var(--white)}
.search::after{content:"";position:absolute;left:6px;top:6px;width:6px;height:6px;border:1.5px solid var(--navy);border-radius:50%}
.sidebar__social{position:absolute;left:8px;top:285px;display:flex;gap:3px}
.sidebar__social span{width:24px;height:24px;border:1.5px solid var(--white);border-radius:50%}
.tile{position:absolute;background:linear-gradient(160deg,var(--photo-a),var(--photo-b))}
.tile--warm{background:linear-gradient(160deg,#8a6fc0,#c8b39a)}
.tile--light{background:linear-gradient(160deg,#d9dbe6,#b79cc1)}
.tile--blue{background:linear-gradient(160deg,#2f5fc4,#d2b091)}
.tile-arrow{position:absolute;width:18px;height:26px;background:var(--white);font-size:12px;text-align:center;line-height:26px;color:#222}

/* bio */
.bio__script{position:absolute;left:96px;top:530px;font-family:"Great Vibes",cursive;font-size:40px;color:#2a6fcf}
.bio__title{position:absolute;left:100px;top:576px;font-family:"Varela Round",sans-serif;font-size:34px;color:var(--ink)}
.bio__ghost{position:absolute;left:306px;top:528px;font-family:"Roboto",sans-serif;font-weight:900;font-size:84px;letter-spacing:1px;color:var(--ghost)}
.bio__text{position:absolute;left:100px;top:632px;width:612px;font-size:9.2px;line-height:18.8px;color:var(--text)}

/* capabilities */
.capabilities{position:absolute;left:0;top:960px;width:804px;height:380px;color:var(--white);text-align:center}
.capabilities svg{position:absolute;left:0;top:0}
.capabilities__badge{position:absolute;left:370px;top:-13px;width:64px;height:64px;border-radius:50%;background:var(--white);font-family:"Varela Round",sans-serif;font-size:15px;color:var(--blue);line-height:64px}
.capabilities__ghost{position:absolute;left:0;right:0;top:94px;font-family:"Roboto",sans-serif;font-weight:900;font-size:62px;color:rgba(20,40,120,.25);letter-spacing:2px}
.capabilities__title{position:absolute;left:0;right:0;top:100px;font-family:"Varela Round",sans-serif;font-size:34px}
.capabilities__lead{position:absolute;left:0;right:0;top:150px;font-size:11.5px}
.capabilities__list{position:absolute;left:0;right:0;top:188px;list-style:none;font-size:10px;line-height:17.6px}

/* contact */
.contact__ghost{position:absolute;left:-114px;top:1505px;width:370px;text-align:center;font-family:"Roboto",sans-serif;font-weight:900;font-size:82px;line-height:84px;color:#f1f1f3;transform:rotate(-90deg)}
.contact__title{position:absolute;left:0;right:0;top:1388px;text-align:center;font-family:"Varela Round",sans-serif;font-size:34px;color:var(--ink)}
.contact__info{position:absolute;left:0;right:0;top:1449px;display:flex;justify-content:center;align-items:center;gap:8px;font-size:11px;color:#222}
.contact__icon{position:relative;width:27px;height:27px;border-radius:50%;background:var(--ink)}
.contact__icon--phone{background:var(--blue);margin-left:10px}
.contact__icon--profile{margin-left:10px}
.contact__icon svg{position:absolute;left:7px;top:7px}
.field{position:absolute;height:36px;border:1px solid var(--field);box-shadow:0 1px 3px rgba(0,0,0,.06);padding:11px 14px;font-size:10.5px;color:#333}
.field--message{height:77px}
.submit{position:absolute;left:328px;top:1710px;width:149px;height:29px;background:var(--blue);color:var(--white);font-size:10.5px;text-align:center;line-height:29px}
.footer{position:absolute;left:0;top:1796px;width:804px;height:54px;background:var(--navy);color:var(--white);font-size:8.5px;text-align:center;line-height:54px}
</style>
</head>
<body>
<div class="stage">

  <!-- Layout A: hexagon gallery -->
  <div class="page page--hex">
    <svg class="hexes" width="804" height="530" viewBox="0 0 804 530">
      <defs>
        <linearGradient id="ph1" x1="0" y1="0" x2="1" y2="1"><stop offset="0" stop-color="#c9c3d6"/><stop offset="1" stop-color="#8d7f9f"/></linearGradient>
        <linearGradient id="ph2" x1="0" y1="0" x2="1" y2="1"><stop offset="0" stop-color="#3c4fc2"/><stop offset=".6" stop-color="#c4a58a"/><stop offset="1" stop-color="#e6dfd8"/></linearGradient>
        <linearGradient id="ph3" x1="0" y1="0" x2="1" y2="1"><stop offset="0" stop-color="#d9c2a8"/><stop offset="1" stop-color="#6f86c8"/></linearGradient>
        <linearGradient id="ph4" x1="0" y1="0" x2="1" y2="1"><stop offset="0" stop-color="#c9a57f"/><stop offset="1" stop-color="#4c6ab8"/></linearGradient>
        <linearGradient id="ph5" x1="0" y1="0" x2="1" y2="1"><stop offset="0" stop-color="#6ab5d8"/><stop offset="1" stop-color="#1d3e6e"/></linearGradient>
      </defs>
      <polygon role="img" aria-label="Photo: holding an award at a PR awards event" fill="url(#ph1)" points="116,57 221,122 221,248 116,313 11,248 11,122"/>
      <polygon role="img" aria-label="Photo: on a broadcast interview with a camera operator" fill="url(#ph3)" points="699,52 804,117 804,248 699,313 583,248 583,117"/>
      <polygon role="img" aria-label="Photo: smiling at a conference booth" fill="url(#ph4)" points="238,267 352,330 352,453 238,516 124,453 124,330"/>
      <polygon role="img" aria-label="Photo: presenting on stage at a health tech conference" fill="url(#ph5)" points="566,267 680,330 680,453 566,516 453,453 453,330"/>
      <polygon role="img" aria-label="Main photo: portrait in a white blazer at the Brintex tower" fill="url(#ph2)" stroke="#fff" stroke-width="10" points="401,15 571,113 571,309 401,407 231,309 231,113"/>
    </svg>
    <span class="arrow" style="left:6px;top:172px">‹</span>
    <span class="arrow" style="left:789px;top:172px">›</span>
    <div class="brand"><span class="brand__mark"></span><span class="brand__name">Harbor<br>Lane<br>Media</span></div>
    <div class="social"><span class="social__dot"></span><span class="social__dot social__dot--b"></span><span class="social__dot social__dot--c"></span></div>
    <div class="burger"></div>

    <div class="content">
      <div class="bio__ghost">BIOGRAPHY</div>
      <div class="bio__script">Bio</div>
      <h2 class="bio__title">About Me</h2>
      <div class="bio__text">
        <p>Dana is a global health industry connector and creative problem solver. She has worked on some of the world's biggest therapies and medical technologies, including the first gene-silencing therapy (Verolith's ONVARA), the first therapy for a rare muscle disorder (Caltris's MYOGEN 51), the first technology in the world to personalize insulin 24 hrs. a day (Arvane's GlucoLink 670) and Kestrel Systems' AI launch into healthcare. She has counseled some of the most well-known health/ technology organizations and developed communications strategies for the world's biggest brands (Norvale, Pellix Labs, Tamsin Health, Orrin Bio, Quarry Retail and more), but she is most proud of her work telling patient stories. Dana excels at working with the media to bring health stories to life while making them accessible to stakeholders. She worked as a journalist before transitioning to communications and has special insight in working with the media. With 15-years of communications experience, she is consistently leveraging her long-standing relationships with global agenda-setting reporters across a range of national broadcast, wire, business and technology outlets, and key health trades, digital health journals and many more.</p>
        <p>Dana also has investor and analyst relations experience (Section 9, Bluewater Ventures, Halden Medicine, Corvia Biosystems, Sable Bio) that adds to her ability to highlight market dynamics. Named a PR Professional of the Year in 2011 for her published research on stakeholder engagement, Dana has built a reputation for her energy, creativity and humor. She received her MA in communications and media studies and her BA in English.</p>
      </div>

      <section class="capabilities">
        <svg width="804" height="380" viewBox="0 0 804 380">
          <defs><linearGradient id="capA" x1="0" y1="0" x2="0" y2="1"><stop offset="0" stop-color="#2350a8"/><stop offset="1" stop-color="#0fa8ea"/></linearGradient></defs>
          <polygon fill="url(#capA)" points="0,64 402,12 804,64 804,322 402,372 0,322"/>
        </svg>
        <div class="capabilities__badge">HLM</div>
        <div class="capabilities__ghost">CAPABILITY</div>
        <h2 class="capabilities__title">Harbor Lane Media Capabilities</h2>
        <p class="capabilities__lead">Providing senior level support for elite pharma/ biotech/ healthcare companies at all stages of development.</p>
        <ul class="capabilities__list">
          <li>Expert Media Relations</li><li>Corporate Thought Leadership</li><li>Executive Visibility</li><li>Narrative Development</li><li>Crisis Management</li><li>Drug/ and Device Product Development</li><li>Narrative Development</li>
        </ul>
      </section>

      <div class="contact__ghost">CONTACT</div>
      <h2 class="contact__title">Contact</h2>
      <div class="contact__info">
        <span class="contact__icon"><svg width="13" height="13" viewBox="0 0 13 13"><rect x="1" y="3" width="11" height="8" fill="#fff"/><path d="M1 3l5.5 4 5.5-4" stroke="#2d3a8c" fill="none"/></svg></span>
        <span>dana@harborlanemedia.com</span>
        <span class="contact__icon contact__icon--phone"><svg width="13" height="13" viewBox="0 0 13 13"><path d="M3 1l2 3-1.3 1.3a7 7 0 0 0 4 4L9 8l3 2-1 2C6 12 1 7 1 2z" fill="#fff"/></svg></span>
        <span>+1-555-014-2290</span>
        <span class="contact__icon contact__icon--profile" role="img" aria-label="Proflume profile"></span>
      </div>
      <div class="field" style="left:156px;top:1514px;width:242px">First Name</div>
      <div class="field" style="left:404px;top:1514px;width:243px">Last Name</div>
      <div class="field" style="left:156px;top:1557px;width:242px">Email address</div>
      <div class="field" style="left:404px;top:1557px;width:243px">Phone Number</div>
      <div class="field field--message" style="left:156px;top:1600px;width:491px">Message</div>
      <div class="submit">SUBMIT MESSAGE ›</div>
      <footer class="footer">Copyrights © 2020, Harbor Lane Media . All rights reserved &nbsp;|&nbsp; Privacy Policy &nbsp;|&nbsp; Terms of use</footer>
    </div>
  </div>

  <!-- Layout B: sidebar with photo grid -->
  <div class="page page--grid">
    <div class="tile tile--light" style="left:101px;top:5px;width:183px;height:154px" role="img" aria-label="Photo: at a trade show floor"></div>
    <div class="tile tile--light" style="left:101px;top:165px;width:183px;height:153px" role="img" aria-label="Photo: holding an award at a PR awards event"></div>
    <div class="tile tile--blue" style="left:290px;top:5px;width:319px;height:313px" role="img" aria-label="Main photo: portrait in a white blazer at the Brintex tower"></div>
    <div class="tile tile--warm" style="left:616px;top:5px;width:182px;height:154px" role="img" aria-label="Photo: at a health tech conference stand"></div>
    <div class="tile" style="left:616px;top:165px;width:182px;height:153px" role="img" aria-label="Photo: with a colleague at an industry event"></div>
    <span class="tile-arrow" style="left:101px;top:149px">‹</span>
    <span class="tile-arrow" style="left:780px;top:149px">›</span>
    <nav class="sidebar">
      <div class="sidebar__brand"><span class="sidebar__mark"></span><span>Harbor<br>Lane<br>Media</span></div>
      <ul class="menu"><li>Home</li><li>About Us</li><li>Capabilities</li><li>Contact</li></ul>
      <span class="search"></span>
      <div class="sidebar__social"><span></span><span></span><span></span></div>
    </nav>

    <div class="content">
      <div class="bio__ghost">BIOGRAPHY</div>
      <div class="bio__script">Bio</div>
      <h2 class="bio__title">About Me</h2>
      <div class="bio__text">
        <p>Dana is a global health industry connector and creative problem solver. She has worked on some of the world's biggest therapies and medical technologies, including the first gene-silencing therapy (Verolith's ONVARA), the first therapy for a rare muscle disorder (Caltris's MYOGEN 51), the first technology in the world to personalize insulin 24 hrs. a day (Arvane's GlucoLink 670) and Kestrel Systems' AI launch into healthcare. She has counseled some of the most well-known health/ technology organizations and developed communications strategies for the world's biggest brands (Norvale, Pellix Labs, Tamsin Health, Orrin Bio, Quarry Retail and more), but she is most proud of her work telling patient stories. Dana excels at working with the media to bring health stories to life while making them accessible to stakeholders. She worked as a journalist before transitioning to communications and has special insight in working with the media. With 15-years of communications experience, she is consistently leveraging her long-standing relationships with global agenda-setting reporters across a range of national broadcast, wire, business and technology outlets, and key health trades, digital health journals and many more.</p>
        <p>Dana also has investor and analyst relations experience (Section 9, Bluewater Ventures, Halden Medicine, Corvia Biosystems, Sable Bio) that adds to her ability to highlight market dynamics. Named a PR Professional of the Year in 2011 for her published research on stakeholder engagement, Dana has built a reputation for her energy, creativity and humor. She received her MA in communications and media studies and her BA in English.</p>
      </div>

      <section class="capabilities">
        <svg width="804" height="380" viewBox="0 0 804 380">
          <defs><linearGradient id="capB" x1="0" y1="0" x2="0" y2="1"><stop offset="0" stop-color="#2350a8"/><stop offset="1" stop-color="#0fa8ea"/></linearGradient></defs>
          <polygon fill="url(#capB)" points="0,64 402,12 804,64 804,322 402,372 0,322"/>
        </svg>
        <div class="capabilities__badge">HLM</div>
        <div class="capabilities__ghost">CAPABILITY</div>
        <h2 class="capabilities__title">Harbor Lane Media Capabilities</h2>
        <p class="capabilities__lead">Providing senior level support for elite pharma/ biotech/ healthcare companies at all stages of development.</p>
        <ul class="capabilities__list">
          <li>Expert Media Relations</li><li>Corporate Thought Leadership</li><li>Executive Visibility</li><li>Narrative Development</li><li>Crisis Management</li><li>Drug/ and Device Product Development</li><li>Narrative Development</li>
        </ul>
      </section>

      <div class="contact__ghost">CONTACT</div>
      <h2 class="contact__title">Contact</h2>
      <div class="contact__info">
        <span class="contact__icon"><svg width="13" height="13" viewBox="0 0 13 13"><rect x="1" y="3" width="11" height="8" fill="#fff"/><path d="M1 3l5.5 4 5.5-4" stroke="#2d3a8c" fill="none"/></svg></span>
        <span>dana@harborlanemedia.com</span>
        <span class="contact__icon contact__icon--phone"><svg width="13" height="13" viewBox="0 0 13 13"><path d="M3 1l2 3-1.3 1.3a7 7 0 0 0 4 4L9 8l3 2-1 2C6 12 1 7 1 2z" fill="#fff"/></svg></span>
        <span>+1-555-014-2290</span>
        <span class="contact__icon contact__icon--profile" role="img" aria-label="Proflume profile"></span>
      </div>
      <div class="field" style="left:156px;top:1514px;width:242px">First Name</div>
      <div class="field" style="left:404px;top:1514px;width:243px">Last Name</div>
      <div class="field" style="left:156px;top:1557px;width:242px">Email address</div>
      <div class="field" style="left:404px;top:1557px;width:243px">Phone Number</div>
      <div class="field field--message" style="left:156px;top:1600px;width:491px">Message</div>
      <div class="submit">SUBMIT MESSAGE ›</div>
      <footer class="footer">Copyrights © 2020, Harbor Lane Media . All rights reserved &nbsp;|&nbsp; Privacy Policy &nbsp;|&nbsp; Terms of use</footer>
    </div>
  </div>

</div>
</body>
</html>
```